Re-design a highly converting profile page for my website

My website allows people to book a mentor for long-term mentorship as well as sessions. I would like to re-design this site within our branding guidelines to give people the best profile possible.

Please give this website a modern look and concentrate on the CTA and conversion rates. This is a highly converting site and it should stay that way or even get better!

Please also keep menu bar & footer in tact

Target Market(s)

Developers, Designers, Entrepreneurs in the Tech industry

Number of Pages Required

1 page

Requirements
Must have
• Strong CTA, existing color palette, testimonials and major elements
Nice to have
• Modern look, easy to see CTA, easy to scan offer. Not too crowded
Should not have
• No reporpusing. It is and stays a profile page

```html
<!DOCTYPE html>
<html lang="en">
<head>
<meta charset="utf-8">
<title>Daniel Harwood – Mentor Profile</title>
<link href="https://fonts.googleapis.com/css2?family=Poppins:wght@300;400;500;600&family=Roboto:wght@400;500;700&display=swap" rel="stylesheet">
<style>
:root{
  --navy:#34435f;
  --navy-dark:#2e3c57;
  --teal:#1ec9a3;
  --teal-dark:#17b392;
  --ink:#2f3b52;
  --body:#5d6372;
  --muted:#8a909c;
  --line:#e4e8ee;
  --soft:#f4f6fa;
  --blue:#1f7fd8;
  --star:#f8c313;
  --foot-text:#b9c1d0;
}
*{box-sizing:border-box;margin:0;padding:0}
html,body{width:1200px;height:3338px;overflow:hidden}
body{font-family:"Poppins",sans-serif;color:var(--body);background:#fff;position:relative}
.abs{position:absolute}
a{color:var(--teal);text-decoration:none}

/* header */
.topbar{position:absolute;left:0;top:0;width:1200px;height:60px;background:var(--navy)}
.brand{position:absolute;left:60px;top:14px;display:flex;align-items:center;gap:8px;color:#fff;font-size:15px;font-weight:500}
.brand-dot{width:32px;height:32px;border-radius:50%;background:var(--teal)}
.nav{position:absolute;left:470px;top:22px;display:flex;gap:24px;font-size:12px;color:#fff}
.nav-star{position:absolute;left:1013px;top:21px}
.btn-logout{position:absolute;left:1042px;top:13px;width:97px;height:34px;border-radius:17px;background:var(--teal);color:#fff;font-weight:600;font-size:15px;display:flex;align-items:center;justify-content:center}

/* profile card */
.profile-card{position:absolute;left:127px;top:114px;width:667px;height:2849px;border:1px solid var(--line);border-radius:4px}
.avatar{position:absolute;left:156px;top:148px;width:134px;height:134px;border-radius:50%;background:radial-gradient(circle at 50% 40%,#e9b9a0,#b9836a 60%,#d77f8e)}
.stars{position:absolute;left:172px;top:305px;display:flex;gap:3px}
.rating{position:absolute;left:150px;top:337px;width:146px;text-align:center;font-size:13px;line-height:19px;color:var(--ink)}
.mentor-name{position:absolute;left:328px;top:162px;font-family:"Roboto",sans-serif;font-size:29px;font-weight:500;color:var(--ink)}
.location{position:absolute;left:330px;top:203px;font-size:12px;color:var(--muted);display:flex;align-items:center;gap:6px}
.spots{position:absolute;left:328px;top:245px;font-size:13px;font-weight:600;letter-spacing:.5px;color:var(--ink)}
.role{position:absolute;left:328px;top:269px;font-size:13.5px;color:var(--ink)}
.social{position:absolute;top:168px;width:38px;height:38px;border-radius:50%}
.social.one{left:687px;background:#1b8be6}
.social.two{left:731px;background:#1e6fc4}
.feature{position:absolute;height:40px;border-radius:20px;box-shadow:0 2px 8px rgba(40,60,90,.12);background:#fff;display:flex;align-items:center;font-size:12px;color:var(--ink)}
.feature .ico{width:42px;height:40px;border-radius:8px;background:var(--teal);display:flex;align-items:center;justify-content:center;margin-right:18px}

/* about */
.about{position:absolute;left:293px;top:457px;width:479px;height:1260px;background:var(--soft);border-top:4px solid var(--teal)}
.about-text{position:absolute;left:336px;width:360px;font-size:11.5px;line-height:19.5px;color:var(--body)}
.quote-box{position:absolute;left:293px;top:813px;width:479px;height:261px;background:var(--teal);color:#fff}
.quote-box p{position:absolute;left:43px;top:44px;width:385px;font-size:12.5px;line-height:21px}
.quote-box .by{position:absolute;left:43px;top:203px;font-size:14px;font-weight:500}
.quote-mark{position:absolute;left:380px;top:160px;font-size:120px;line-height:1;font-family:"Roboto",sans-serif;color:rgba(255,255,255,.3)}
.dots{position:absolute;left:508px;top:1094px;display:flex;gap:5px}
.dots i{width:10px;height:10px;border-radius:50%;border:1.3px solid #7a8294}
.dots i.on{background:var(--teal);border-color:var(--teal)}
.extra{position:absolute;left:336px;font-size:12.5px;color:var(--ink)}
.dotted{position:absolute;left:332px;top:1311px;width:407px;border-top:1.5px dotted #a9afbb}

/* testimonials */
.testimonial{position:absolute;left:293px;width:479px;background:#fff;border:1px solid var(--line)}
.testimonial p{position:absolute;left:42px;top:38px;width:420px;font-size:11.5px;line-height:21px}
.testimonial .sig{position:absolute;left:42px;display:flex;align-items:center;gap:12px;font-family:"Roboto",sans-serif;font-size:12px;font-weight:500;color:var(--ink)}

/* related */
.related-title{position:absolute;left:297px;top:2514px;font-family:"Roboto",sans-serif;font-size:26px;font-weight:500;color:var(--navy)}
.mentor-card{position:absolute;top:2573px;height:336px;border:1px solid var(--line);background:#fff}
.mentor-card .pic{position:absolute;left:14px;top:30px;width:42px;height:42px;border-radius:50%;background:radial-gradient(circle at 50% 45%,#c9896a,#5a3a2c)}
.mentor-card h3{position:absolute;left:68px;top:26px;font-family:"Roboto",sans-serif;font-size:17px;font-weight:500;color:var(--ink)}
.mentor-card .sub{position:absolute;left:69px;top:52px;font-size:11.5px;color:var(--body)}
.mentor-card .price{position:absolute;left:68px;top:80px;width:127px;height:30px;border-radius:15px;background:var(--teal);color:#fff;font-family:"Roboto",sans-serif;font-weight:500;font-size:13px;display:flex;align-items:center;justify-content:center}
.mentor-card .blurb{position:absolute;left:19px;top:124px;width:190px;font-size:11.5px;line-height:20px;color:var(--ink)}
.mentor-card ul{position:absolute;left:20px;top:182px;list-style:none}
.mentor-card li{height:29px;font-size:11.5px;color:var(--body)}

/* arrow bullet */
.bullet{display:flex;align-items:center}
.bullet::before{content:"›";flex:none;width:12px;height:12px;border:1.3px solid var(--teal);border-radius:50%;color:var(--teal);font-size:10px;line-height:9px;text-align:center;margin-right:11px}

/* sidebar */
.side-card{position:absolute;left:822px;width:250px;border:1px solid var(--line);border-radius:3px;background:#fff}
.side-card h4{position:absolute;left:32px;font-family:"Roboto",sans-serif;font-size:16.5px;font-weight:500;line-height:22px;color:var(--ink)}
.side-card .note{position:absolute;left:35px;font-size:11px;line-height:19px;color:var(--body)}
.btn{position:absolute;left:32px;height:36px;border-radius:18px;background:var(--teal);color:#fff;font-family:"Roboto",sans-serif;font-weight:500;font-size:14px;display:flex;align-items:center;justify-content:center}
.skills{position:absolute;left:32px;top:97px;list-style:none}
.skills li{height:34.6px;font-family:"Roboto",sans-serif;font-size:12px;font-weight:500;color:var(--ink)}
.skills li.faint{color:var(--muted);font-weight:400}
.skills .gap{margin-left:38px}

/* footer */
.footer{position:absolute;left:0;top:3017px;width:1200px;height:321px;background:var(--navy)}
.footer .brand{top:50px}
.foot-about{position:absolute;left:60px;top:103px;width:260px;font-size:11.5px;line-height:21px;color:var(--foot-text)}
.foot-social{position:absolute;top:175px;width:38px;height:38px;border-radius:50%;background:#1b8be6}
.foot-col{position:absolute;top:52px}
.foot-col h5{font-family:"Roboto",sans-serif;font-size:15px;font-weight:500;color:#fff;margin-bottom:14px}
.foot-col ul{list-style:none}
.foot-col li{font-size:11.5px;line-height:21px;color:var(--foot-text);display:flex;align-items:center}
.foot-col li::before{content:"";width:4px;height:4px;border-radius:50%;background:var(--teal);margin-right:14px}
.foot-rule{position:absolute;left:60px;top:275px;width:1080px;border-top:1px solid #45546f}
.copyright{position:absolute;left:0;top:290px;width:1200px;text-align:center;font-size:11px;color:var(--foot-text)}
</style>
</head>
<body>

<header class="topbar">
  <div class="brand"><span class="brand-dot"></span>Mentor Harbor</div>
  <nav class="nav"><span>Dashboard</span><span>Management</span><span>Your Profile</span></nav>
  <svg class="nav-star" width="17" height="17" viewBox="0 0 24 24"><path fill="var(--star)" d="M12 2l3 6.9 7.5.7-5.7 5 1.7 7.4L12 18.3 5.5 22l1.7-7.4-5.7-5 7.5-.7z"/></svg>
  <div class="btn-logout">Logout</div>
</header>

<main>
  <section class="profile-card"></section>

  <div class="avatar" role="img" aria-label="Portrait photo of the mentor"></div>
  <div class="stars">
    <svg width="18" height="18" viewBox="0 0 24 24"><path fill="var(--star)" d="M12 2l3 6.9 7.5.7-5.7 5 1.7 7.4L12 18.3 5.5 22l1.7-7.4-5.7-5 7.5-.7z"/></svg>
    <svg width="18" height="18" viewBox="0 0 24 24"><path fill="var(--star)" d="M12 2l3 6.9 7.5.7-5.7 5 1.7 7.4L12 18.3 5.5 22l1.7-7.4-5.7-5 7.5-.7z"/></svg>
    <svg width="18" height="18" viewBox="0 0 24 24"><path fill="var(--star)" d="M12 2l3 6.9 7.5.7-5.7 5 1.7 7.4L12 18.3 5.5 22l1.7-7.4-5.7-5 7.5-.7z"/></svg>
    <svg width="18" height="18" viewBox="0 0 24 24"><path fill="var(--star)" d="M12 2l3 6.9 7.5.7-5.7 5 1.7 7.4L12 18.3 5.5 22l1.7-7.4-5.7-5 7.5-.7z"/></svg>
    <svg width="18" height="18" viewBox="0 0 24 24"><path fill="var(--star)" d="M12 2l3 6.9 7.5.7-5.7 5 1.7 7.4L12 18.3 5.5 22l1.7-7.4-5.7-5 7.5-.7z"/></svg>
  </div>
  <div class="rating">5.0<br>(5 Reviews)</div>

  <h1 class="mentor-name">Daniel Harwood</h1>
  <div class="location">
    <svg width="12" height="15" viewBox="0 0 12 15"><path d="M6 1a4.5 4.5 0 0 0-4.5 4.5C1.5 9 6 13.5 6 13.5S10.5 9 10.5 5.5A4.5 4.5 0 0 0 6 1z" fill="none" stroke="var(--teal)" stroke-width="1.3"/><circle cx="6" cy="5.5" r="1.6" fill="none" stroke="var(--teal)" stroke-width="1.3"/></svg>
    United States of America
  </div>
  <div class="spots">[2 SPOST AVAILABLE]</div>
  <div class="role">Director of Product - Brightline Insurance</div>
  <span class="social one" role="img" aria-label="Social profile link"></span>
  <span class="social two" role="img" aria-label="Social profile link"></span>

  <div class="feature" style="left:323px;top:318px;width:199px">
    <span class="ico"><svg width="20" height="18" viewBox="0 0 20 18"><path d="M2 2h16v10H8l-4 4v-4H2z" fill="none" stroke="#fff" stroke-width="1.4"/><path d="M5 6h10M5 9h7" stroke="#fff" stroke-width="1.2"/></svg></span>Personal Chat</div>
  <div class="feature" style="left:533px;top:318px;width:198px">
    <span class="ico"><svg width="18" height="20" viewBox="0 0 18 20"><rect x="2" y="2" width="14" height="16" rx="1.5" fill="none" stroke="#fff" stroke-width="1.4"/><path d="M5 7h8M5 10h8M5 13h5" stroke="#fff" stroke-width="1.2"/></svg></span>To-Dos &amp; Goals</div>
  <div class="feature" style="left:323px;top:370px;width:199px">
    <span class="ico"><svg width="20" height="20" viewBox="0 0 20 20"><path d="M6 2h8v5a4 4 0 0 1-8 0z" fill="none" stroke="#fff" stroke-width="1.4"/><path d="M6 4H3a3 3 0 0 0 3 4M14 4h3a3 3 0 0 1-3 4M10 11v4M6 18h8" fill="none" stroke="#fff" stroke-width="1.4"/></svg></span>Challenges &amp; Projects</div>
  <div class="feature" style="left:533px;top:370px;width:196px">
    <span class="ico"><svg width="18" height="18" viewBox="0 0 24 24"><path d="M6.6 10.8a15 15 0 0 0 6.6 6.6l2.2-2.2a1 1 0 0 1 1-.25 11.4 11.4 0 0 0 3.6.57 1 1 0 0 1 1 1V20a1 1 0 0 1-1 1A17 17 0 0 1 3 4a1 1 0 0 1 1-1h3.5a1 1 0 0 1 1 1c0 1.25.2 2.45.57 3.57a1 1 0 0 1-.25 1z" fill="none" stroke="#fff" stroke-width="1.5"/></svg></span>1- on-1 Calls</div>

  <section class="about"></section>
  <p class="about-text" style="top:497px">Daniel Harwood is passionate about creating and scaling powerful web and mobile products that make a significant impact in millions of people's lives around the world. Daniel deeply enjoys building and managing the product and development teams that help achieveth at goal.</p>
  <p class="about-text" style="top:614px;width:370px">Daniel is currently the Director of Product at Brightline Insurance (<a>www.brightlineins.com</a>). He was previously the CPO of Lumenreach Media (<a>www.lumenreach.com</a>) which operated in the Ad Tech industry, helping the world's largest media companies with data-inspired storytelling. Previously a Senior Product leader at Northpass Travel (<a>www.northpass.com</a>) and Printwell Digital (<a>www.printwell.com/digital</a>).</p>

  <blockquote class="quote-box">
    <p>"Daniel helped me set focus and intention in my goal of scaling my independent projects. Before working with Daniel I felt like I was jumping from idea to idea with no plan. During our session he proved clear action items which I enjoyed completing. Each week were viewed the progress and established new items to iterate towards my goal. I am very thank ful for my mentoring sessions with Daniel "</p>
    <span class="by">— &nbsp;Ronan</span>
    <span class="quote-mark">”</span>
  </blockquote>
  <div class="dots"><i></i><i></i><i class="on"></i><i></i><i></i></div>

  <div class="extra" style="top:1174px;font-size:14px">Aspiring or new PM? Or looking to level up ?</div>
  <div class="extra" style="top:1199px">Check out my new Product Management course here:</div>
  <div class="extra" style="top:1224px"><a style="font-weight:500">www.productcraftlab.co</a> &nbsp;<span style="font-size:11.5px">(Use 25 PCT TO &nbsp;FFMENTOR</span></div>
  <div class="extra" style="top:1249px">for 25 % off my Course!)</div>
  <div class="dotted"></div>
  <div class="extra" style="top:1348px">Author: Shipping Better Products</div>
  <div class="extra" style="top:1370px"><a>(www.ShippingBetterProducts.com)</a></div>
  <div class="extra" style="top:1402px">Author: Rethinking Yourself</div>
  <div class="extra" style="top:1424px"><a>(www.rethinkyourself.co)</a></div>
  <div class="extra" style="top:1453px;font-size:14.5px">Website: &nbsp;<a style="font-size:12.5px">www.theproductcraftlab.com</a></div>
  <div class="extra" style="top:1488px;font-size:14.5px">Blog: &nbsp;<a style="font-size:12.5px">https://notes.productcraftlab.co/@dharwood</a></div>
  <div class="extra" style="top:1511px">Top Writer in Inkwell startup Category</div>
  <div class="extra" style="top:1534px"><a>(https://inkwell.pub/tag/startup/top-writers)</a></div>
  <div class="extra" style="top:1573px">The Product Craft Lab Newsletter:</div>
  <div class="extra" style="top:1591px"><a>https://go.productcraftlab.co/newsletter</a></div>
  <div class="extra" style="top:1611px">The Product Craft Lab Video Channel:</div>
  <div class="extra" style="top:1634px;width:340px;line-height:18px"><a>https://www.videohub.tv/channel/PCL_-kY0qhi-G9nV5XUxbHfhx</a></div>

  <article class="testimonial" style="top:1734px;height:246px">
    <p>Daniel helped me set focus and intention in my goal of scaling my independent project. Before working with Daniel, I felt like I Was jumping from idea to idea with no plan. During our session he provided clear action items which I enjoyed completing. Each week we revied the progress and Established new items to iterate towards my goal. i am very thankful for my mentoring sessions with Daniel.</p>
    <div class="sig" style="top:187px"><svg width="20" height="18" viewBox="0 0 20 18"><path d="M1 7h4v10H1zM6 8l4-7c1.5 0 2 1 2 2l-1 4h6a2 2 0 0 1 2 2.3l-1.3 6A2 2 0 0 1 15.7 17H6z" fill="var(--teal)"/></svg>Testimonial by Ronan from September 2020</div>
  </article>
  <article class="testimonial" style="top:1997px;height:245px">
    <p>Daniel is a fantastic mentor and I definitely recommaend him to any Product manger or aspiring PMs. Daniel Worked with men on my resume since I wasn't getteing any callbacks. the results were almost instantaneous as I got my 1st Callback from a Recruiter after only 2 hours of applying with the resume he helped me with. i can't Recommend Daniel enough.</p>
    <div class="sig" style="top:185px"><svg width="20" height="18" viewBox="0 0 20 18"><path d="M1 7h4v10H1zM6 8l4-7c1.5 0 2 1 2 2l-1 4h6a2 2 0 0 1 2 2.3l-1.3 6A2 2 0 0 1 15.7 17H6z" fill="var(--teal)"/></svg>Testimonial by Samir from September 2020</div>
  </article>
  <article class="testimonial" style="top:2259px;height:223px;left:294px">
    <p>Before Working with Daniel, I felt like I was jumping from idea to idea with no plan. During our session he proved clear action items which I enjoyed completing. each week we reviewed the progress and established new items to iterate towards my goal. i am very thankful for my mentoring sessions with Daniel.</p>
    <div class="sig" style="top:166px"><svg width="20" height="18" viewBox="0 0 20 18"><path d="M1 7h4v10H1zM6 8l4-7c1.5 0 2 1 2 2l-1 4h6a2 2 0 0 1 2 2.3l-1.3 6A2 2 0 0 1 15.7 17H6z" fill="var(--teal)"/></svg>Testimonial by Ronan From October 2020</div>
  </article>

  <h2 class="related-title">Related Mentors</h2>
  <article class="mentor-card" style="left:295px;width:230px">
    <div class="pic" role="img" aria-label="Photo of the mentor"></div>
    <h3>Theo Marlowe</h3>
    <div class="sub">Product Manager</div>
    <div class="price">$180 Per Month</div>
    <p class="blurb">We believe Theo could be a good match for you too.</p>
    <ul><li class="bullet">Minimal Viable Products</li><li class="bullet">Team Leadership</li><li class="bullet">Architecture</li><li class="bullet">Web Development</li></ul>
  </article>
  <article class="mentor-card" style="left:543px;width:231px">
    <div class="pic" role="img" aria-label="Photo of the mentor"></div>
    <h3>Kofi Adeyemi</h3>
    <div class="sub">Software Product Manager</div>
    <div class="price">$140 per month</div>
    <p class="blurb">We believe Kofi could be a good match for you too.</p>
    <ul><li class="bullet">Remote Work</li><li class="bullet">Agile Product Mangement</li><li class="bullet">Product Development lifecycle</li><li class="bullet">Freelance Pm</li><li class="bullet">Team Collection</li></ul>
  </article>
</main>

<aside>
  <section class="side-card" style="top:114px;height:325px">
    <div class="abs" style="left:26px;top:37px;display:flex;align-items:center;gap:6px;font-family:Roboto,sans-serif;font-size:11.5px;font-weight:500;color:var(--blue)">
      <svg width="13" height="13" viewBox="0 0 14 14"><path d="M1 1h6l6 6-6 6-6-6z" fill="var(--blue)"/><circle cx="4" cy="4" r="1.2" fill="#fff"/></svg>7 Day Trial !</div>
    <div class="abs" style="left:27px;top:56px;font-family:Roboto,sans-serif;font-size:36px;font-weight:500;color:var(--ink)">$240/<span style="font-size:22px;color:var(--teal);font-weight:400">mo</span></div>
    <h4 style="top:124px">Personal Mentorship</h4>
    <p class="note" style="top:154px;width:190px">Continuos and personal 1-to-1 Mentorship for a flat fee.</p>
    <div class="abs" style="left:32px;top:217px;font-family:Roboto,sans-serif;font-size:16px;font-weight:500;color:var(--teal);text-decoration:underline">What's Included ?</div>
    <div class="btn" style="top:260px;width:188px">Apply For mentorship</div>
  </section>

  <section class="side-card" style="top:461px;height:195px">
    <h4 style="top:34px;width:205px">"Other(60MinuteSession) "Session</h4>
    <p class="note" style="top:86px">60 minutes, $150 per session</p>
    <div class="btn" style="top:125px;width:135px">Book Session</div>
  </section>

  <section class="side-card" style="top:678px;height:247px">
    <h4 style="top:33px;width:190px">" How to Become a Products Manager - Coaching Seeion (60 Minutes Session)</h4>
    <p class="note" style="top:138px">60 minutes, $150 per session</p>
    <div class="btn" style="top:167px;width:135px">Book Session</div>
  </section>

  <div class="abs" style="left:863px;top:965px;display:flex;align-items:center;gap:10px;font-family:Roboto,sans-serif;font-size:13px;font-weight:500;color:var(--ink)">
    <span style="text-decoration:underline">Shaow All Sessions</span>
    <svg width="26" height="8" viewBox="0 0 26 8"><path d="M0 4h24M20 1l4 3-4 3" fill="none" stroke="#9aa1ad" stroke-width="1"/></svg>
  </div>

  <section class="side-card" style="top:1024px;height:157px">
    <h4 style="top:33px;width:160px">Average Response Time</h4>
    <svg class="abs" style="left:34px;top:96px" width="12" height="20" viewBox="0 0 12 20"><path d="M8 0L1 11h4l-2 9 8-12H7z" fill="var(--teal)"/></svg>
    <p class="note" style="left:55px;top:91px;width:160px;line-height:17px">Usually Responds with in a few hours</p>
  </section>

  <section class="side-card" style="top:1200px;height:157px">
    <h4 style="top:32px;width:140px">Part of These groups</h4>
    <div class="abs" style="left:34px;top:92px;display:flex;align-items:center;gap:7px;font-size:13px;color:var(--teal)">
      <svg width="14" height="14" viewBox="0 0 16 16"><path d="M7 9a3 3 0 0 0 4 0l3-3a3 3 0 0 0-4-4l-1 1M9 7a3 3 0 0 0-4 0L2 10a3 3 0 0 0 4 4l1-1" fill="none" stroke="var(--teal)" stroke-width="1.5"/></svg>Mentors For Startups</div>
  </section>

  <section class="side-card" style="top:1376px;height:848px">
    <h4 style="top:28px;width:140px">Skill Taught By Mentor</h4>
    <ul class="skills">
      <li class="bullet faint">Product &amp; Marketing</li>
      <li class="bullet">Product</li>
      <li class="bullet">Product Manager</li>
      <li class="bullet">Interview</li>
      <li class="bullet">StartUp<span class="gap">Tech</span></li>
      <li class="bullet">Media</li>
      <li class="bullet">Interview<span class="gap">Pm</span></li>
      <li class="bullet">Project Manger</li>
      <li class="bullet">Project Management</li>
      <li class="bullet">Interview Prep</li>
      <li class="bullet">Mock Interview</li>
      <li class="bullet">Product interview</li>
      <li class="bullet">Product Market Fit</li>
      <li class="bullet">Product Pricing</li>
      <li class="bullet">Associate Product Manager</li>
      <li class="bullet">Junior Product Manager</li>
      <li class="bullet">New Product Manger</li>
      <li class="bullet">B2b<span style="margin-left:20px">B2c</span></li>
      <li class="bullet">Mobile Apps<span class="gap">Ios</span></li>
      <li class="bullet">Android</li>
    </ul>
  </section>
</aside>

<footer class="footer">
  <div class="brand"><span class="brand-dot" style="width:44px;height:44px"></span>Mentor Harbor</div>
  <p class="foot-about">Your trusted source to find highly - vetted mentors &amp; industry professionals to move your career ahead.</p>
  <span class="foot-social" style="left:60px" role="img" aria-label="Social profile link"></span>
  <span class="foot-social" style="left:104px;background:#1e6fc4" role="img" aria-label="Social profile link"></span>
  <div class="foot-col" style="left:378px">
    <h5>Sitemap</h5>
    <ul><li>Browse</li><li>Mentors</li><li>Become A mentor</li><li>Partner</li><li>Program</li><li>Faq</li><li>Blog</li></ul>
  </div>
  <div class="foot-col" style="left:610px">
    <h5>Quick Links</h5>
    <ul><li>About Us</li><li>Code Of Conduct</li><li>Privacy Policy</li><li>Success Stories</li></ul>
  </div>
  <div class="foot-col" style="left:841px">
    <h5>Contact Us</h5>
    <div style="display:flex;align-items:center;gap:12px;font-size:11.5px;color:var(--foot-text);margin-top:-2px">
      <svg width="16" height="12" viewBox="0 0 16 12"><rect width="16" height="12" rx="1.5" fill="var(--teal)"/><path d="M1 1l7 5 7-5" fill="none" stroke="var(--navy)" stroke-width="1.3"/></svg>info@mentorharbor.com</div>
  </div>
  <div class="foot-rule"></div>
  <p class="copyright">©<span style="color:var(--teal)">Mentor Harbor</span> - All Rights Reserved.</p>
</footer>

</body>
</html>
```